Copper Lantern Fitness Flyer

We need a Flyer designed for a Revolutionary Fresh New Functional Fitness facility in Manly Sydney, Australia. We have just recently opened and now need to get the word out. Using the flyers to hand out at events also for shop counters and letterbox drops.

Our company name is Copper Lantern Fitness "Where STRENGTH Becomes Your SPARK".
We promote health and fitness to all fitness levels concentrating on functional fitness. To learn more about us and our colour scheme see attached file and also check us out on www.brightvine-social.example/copperlanternfitnessgroup

A5 Size please

Target Market(s)

The beauty of our system is it is for everyone we have girls and guys in there teens, 20's 30's 40's and 50's. Not only that we have professional athletes, military and high fitness levels all the way to people who are overweight and need to loose weight and tone up. The system caters for everyone.

Industry/Entity Type

Fitness

Requirements
Must have
• FRONT:

Free 30min Fat Blasting Experience With Your Very Own Personal Trainer !!!

New Class Starts Every 3 minutes.
30 minute Workout With A Trainer.
No Machines No Mirrors And No Attitudes.
Catering For All Fitness Levels.
Results Guaranteed Or Your Money Back.
Fun, Fresh, Clean, Revolutionary New Facility.

Back:

You Are Just Moments Away From Burning Fat Faster Than Ever Before And Getting That Body You Always Wanted !!!

Come In Today To Claim Your FREE Workout.

Ph (02) 9417 2086
Address 5/127 Greywattle Ave Fernbrook 2178
www.brightvine-social.example/copperlanternfitnessgroup
Nice to have
• FRONT:

Back:

Ph (02) 9417 2086

```html
<!DOCTYPE html>
<html lang="en">
<head>
<meta charset="utf-8">
<title>Copper Lantern Fitness Flyer</title>
<link rel="stylesheet" href="https://fonts.googleapis.com/css2?family=Roboto+Condensed:ital,wght@0,400;0,700;1,900&family=Montserrat:wght@600&display=swap">
<style>
  :root {
    --page: #ececec;
    --paper: #ffffff;
    --blue-deep: #0b3d9c;
    --blue: #1560d6;
    --blue-light: #49a6f0;
    --sky: #7cc4f5;
    --orange-deep: #f08a00;
    --orange: #f7a21b;
    --orange-light: #fcc54a;
    --rust: #b5350f;
    --ink: #2c2c2c;
    --grey: #5a5a5a;
    --logo-mark: #2f8f4e;
  }
  * { margin: 0; padding: 0; box-sizing: border-box; }
  html, body { width: 1200px; height: 848px; overflow: hidden; }
  body {
    background: var(--page);
    font-family: "Roboto Condensed", Arial, sans-serif;
    position: relative;
  }
  .flyer {
    position: absolute;
    top: 133px;
    width: 395px;
    height: 558px;
    background: var(--paper);
    overflow: hidden;
  }
  .flyer--front { left: 172px; }
  .flyer--back { left: 655px; }
  .layer { position: absolute; }

  /* FRONT */
  .front-band { left: 0; top: 0; width: 395px; height: 240px; }
  .headline {
    left: 22px; top: 58px;
    width: 360px;
    transform: rotate(-8deg);
    transform-origin: left top;
    color: #fff;
    font-style: italic;
    font-weight: 900;
    text-transform: uppercase;
  }
  .headline__main { font-size: 38px; line-height: 34px; letter-spacing: 0.5px; }
  .headline__sub { font-size: 11.5px; font-weight: 700; letter-spacing: 0.4px; margin-top: 4px; }
  .pose-icon { left: 222px; top: 4px; width: 34px; height: 22px; background: rgba(255,255,255,0.85); border-radius: 50% 50% 40% 40%; }
  .photo-class {
    left: 0; top: 165px; width: 222px; height: 178px;
    background: linear-gradient(135deg, #c9a98a 0%, #e7c59a 45%, #9a7d6b 100%);
    clip-path: polygon(0 8%, 100% 0, 86% 100%, 0 100%);
  }
  .photo-gym {
    left: 200px; top: 128px; width: 195px; height: 185px;
    background: linear-gradient(160deg, #d8dde2 0%, #a9b3bb 50%, #6d7882 100%);
    clip-path: polygon(18% 6%, 100% 0, 100% 94%, 0 100%);
  }
  .silhouette-front {
    left: 238px; top: 262px; width: 150px; height: 280px;
    background: linear-gradient(180deg, var(--sky) 0%, var(--blue) 100%);
    border-radius: 48% 40% 10% 20%;
    opacity: 0.9;
  }
  .brand { display: flex; align-items: center; gap: 8px; }
  .brand__mark { width: 40px; height: 40px; background: var(--logo-mark); flex: none; }
  .brand__name {
    font-family: "Montserrat", Arial, sans-serif;
    font-weight: 600; text-transform: uppercase;
    color: var(--ink); font-size: 17px; line-height: 17px;
  }
  .brand__tag { font-size: 7px; color: var(--grey); margin-top: 3px; }
  .brand--front { left: 14px; top: 372px; }
  .perks { left: 18px; top: 450px; list-style: none; width: 212px; }
  .perks li {
    display: flex; align-items: center; gap: 6px;
    font-size: 9px; color: var(--grey); line-height: 15px;
    white-space: nowrap;
  }
  .perks svg { width: 11px; height: 11px; flex: none; }

  /* BACK */
  .photo-trainer {
    left: 0; top: 0; width: 395px; height: 270px;
    background: linear-gradient(120deg, #8c6a4a 0%, #c79a6e 40%, #e6cfb3 70%, #b9a493 100%);
  }
  .back-band { left: 0; top: 180px; width: 395px; height: 378px; }
  .silhouette-back {
    left: 18px; top: 452px; width: 140px; height: 34px;
    background: var(--orange-deep);
    border-radius: 40% 60% 20% 20%;
  }
  .pitch {
    left: 40px; top: 392px; width: 220px;
    font-size: 8.3px; line-height: 10px;
    color: var(--rust); text-transform: uppercase;
  }
  .pitch__cta { text-transform: none; font-weight: 700; margin-top: 1px; }
  .brand--back { left: 278px; top: 392px; width: 110px; flex-direction: column; align-items: center; gap: 8px; text-align: center; }
  .brand--back .brand__mark { width: 46px; height: 46px; }
  .brand--back .brand__name { font-size: 14px; line-height: 15px; }
  .brand--back .brand__tag { font-size: 6.5px; }
  .contact {
    left: 18px; top: 506px;
    font-size: 6.8px; line-height: 10px; color: var(--rust);
  }
</style>
</head>
<body>

<section class="flyer flyer--front">
  <svg class="layer front-band" viewBox="0 0 395 240" aria-hidden="true">
    <defs>
      <linearGradient id="blueFill" x1="0" y1="0" x2="1" y2="1">
        <stop offset="0" stop-color="#0b3d9c"/>
        <stop offset="0.6" stop-color="#1560d6"/>
        <stop offset="1" stop-color="#49a6f0"/>
      </linearGradient>
    </defs>
    <polygon points="0,0 395,0 395,128 0,185" fill="url(#blueFill)"/>
    <polygon points="0,40 395,-20 395,0 0,58" fill="#49a6f0" opacity="0.45"/>
    <polygon points="0,150 395,95 395,108 0,165" fill="#7cc4f5" opacity="0.5"/>
    <polygon points="0,170 395,115 395,122 0,177" fill="#ffffff" opacity="0.35"/>
  </svg>
  <div class="layer pose-icon" role="img" aria-label="Small white figure in a fitness pose"></div>
  <div class="layer headline">
    <div class="headline__main">Free 30min<br>Fat Blasting</div>
    <div class="headline__sub">Experience with your very own personal trainer!!!</div>
  </div>
  <div class="layer photo-class" role="img" aria-label="Photo of a smiling woman leading a group fitness class"></div>
  <div class="layer photo-gym" role="img" aria-label="Photo of a bright gym floor with training equipment"></div>
  <div class="layer silhouette-front" role="img" aria-label="Blue silhouette illustration of a woman doing a lunge stretch"></div>

  <div class="layer brand brand--front">
    <div class="brand__mark"></div>
    <div>
      <div class="brand__name">Copper<br>Lantern<br>Fitness</div>
      <div class="brand__tag">Where Strength Becomes Your Spark</div>
    </div>
  </div>

  <ul class="layer perks">
    <li><svg viewBox="0 0 12 12"><path d="M2 6.5l2.5 2.5L10 3" fill="none" stroke="#1560d6" stroke-width="2"/></svg>New Class Starts Every 3 minutes.</li>
    <li><svg viewBox="0 0 12 12"><path d="M2 6.5l2.5 2.5L10 3" fill="none" stroke="#1560d6" stroke-width="2"/></svg>30 minute Workout With A Trainer.</li>
    <li><svg viewBox="0 0 12 12"><path d="M2 6.5l2.5 2.5L10 3" fill="none" stroke="#1560d6" stroke-width="2"/></svg>No Machines No Mirrors And No Attitudes.</li>
    <li><svg viewBox="0 0 12 12"><path d="M2 6.5l2.5 2.5L10 3" fill="none" stroke="#1560d6" stroke-width="2"/></svg>Catering For All Fitness Levels.</li>
    <li><svg viewBox="0 0 12 12"><path d="M2 6.5l2.5 2.5L10 3" fill="none" stroke="#1560d6" stroke-width="2"/></svg>Results Guaranteed Or Your Money Back.</li>
    <li><svg viewBox="0 0 12 12"><path d="M2 6.5l2.5 2.5L10 3" fill="none" stroke="#1560d6" stroke-width="2"/></svg>Fun, Fresh, Clean, Revolutionary New Facility.</li>
  </ul>
</section>

<section class="flyer flyer--back">
  <div class="layer photo-trainer" role="img" aria-label="Photo of a personal trainer guiding a woman lifting dumbbells"></div>
  <svg class="layer back-band" viewBox="0 0 395 378" aria-hidden="true">
    <defs>
      <linearGradient id="orangeFill" x1="0" y1="0" x2="0" y2="1">
        <stop offset="0" stop-color="#f7a21b"/>
        <stop offset="0.5" stop-color="#fcc54a"/>
        <stop offset="1" stop-color="#f7a21b"/>
      </linearGradient>
    </defs>
    <polygon points="0,58 395,0 395,378 0,378" fill="#f08a00"/>
    <polygon points="0,72 395,18 395,40 0,95" fill="#fcc54a" opacity="0.8"/>
    <polygon points="0,100 395,46 395,378 0,378" fill="url(#orangeFill)"/>
    <polygon points="0,118 395,70 395,78 0,126" fill="#ffffff" opacity="0.3"/>
  </svg>
  <div class="layer silhouette-back" role="img" aria-label="Orange silhouette illustration of a woman in a yoga stretch"></div>
  <div class="layer pitch">
    You are just moments<br>away from burning fat faster<br>than ever before and getting that<br>body you always wanted!!!
    <div class="pitch__cta">Come In Today To Claim Your FREE Workout.</div>
  </div>
  <div class="layer brand brand--back">
    <div class="brand__mark"></div>
    <div>
      <div class="brand__name">Copper<br>Lantern<br>Fitness</div>
      <div class="brand__tag">Where Strength Becomes Your Spark</div>
    </div>
  </div>
  <div class="layer contact">
    Ph (02) 9417 2086 • Address 5/127 Greywattle Ave Fernbrook 2178<br>
    www.brightvine-social.example/copperlanternfitnessgroup
  </div>
</section>

</body>
</html>
```